Rebrand of an existing product label

We are looking for a new design / label for our body lotion. Attached is the current product label. We have this product available in Retinol, Collagen, Hyaluronic Acid, Vitamin C, and Coconut. The brand should reflect a clinical, trustworthy look. We also want to include on the label that the product contains Dead Sea Minerals. Attached is the dieline for the label for the jar and the top. This jar is the packaging that needs to be used for this project.

Target Market(s)

40+

Requirements
Must have
• Ingredient callouts on the front + benefits. Ex- Vitamin C Brightening Cream

```html
<!DOCTYPE html>
<html lang="en">
<head>
<meta charset="utf-8">
<title>Velaine Collagen Body Lotion Label</title>
<link rel="stylesheet" href="https://fonts.googleapis.com/css2?family=Montserrat:wght@400;500;600;700&family=Great+Vibes&display=swap">
<style>
  :root {
    --canvas: #f4f4f5;
    --blush: #fbe3ee;
    --blush-deep: #f5c6db;
    --magenta: #d6409a;
    --magenta-dark: #a91f72;
    --plum: #3a1d2e;
    --mauve: #8a3b63;
    --white: #ffffff;
    --ink: #231a20;
  }
  * { box-sizing: border-box; margin: 0; padding: 0; }
  html, body { width: 1200px; height: 1200px; overflow: hidden; }
  body {
    background: var(--canvas);
    font-family: "Montserrat", Arial, sans-serif;
    position: relative;
  }

  /* Lid label */
  .lid-label {
    position: absolute;
    left: 410px; top: 40px;
    width: 380px; height: 380px;
  }
  .lid-label svg { position: absolute; inset: 0; }
  .lid-text {
    position: absolute;
    left: 0; right: 0; top: 200px;
    text-align: center;
  }
  .lid-script {
    font-family: "Great Vibes", cursive;
    font-size: 38px;
    color: var(--plum);
    line-height: 1;
  }
  .lid-title {
    font-weight: 600;
    font-size: 30px;
    letter-spacing: 1px;
    color: var(--magenta-dark);
    margin-top: 2px;
  }
  .lid-benefit {
    font-weight: 700;
    font-size: 13px;
    letter-spacing: 0.5px;
    color: var(--white);
    margin-top: 26px;
    line-height: 1.4;
  }

  /* Front label */
  .front-label {
    position: absolute;
    left: 100px; top: 480px;
    width: 1000px; height: 640px;
    overflow: hidden;
  }
  .front-label svg.label-bg { position: absolute; inset: 0; }
  .brand {
    position: absolute;
    top: 150px; left: 0; right: 0;
    display: flex; justify-content: center; align-items: center; gap: 18px;
    font-weight: 500;
    font-size: 56px;
    letter-spacing: 2px;
    color: var(--ink);
  }
  .brand-dot {
    width: 22px; height: 22px;
    border-radius: 50%;
    background: var(--ink);
  }
  .size-tag {
    position: absolute;
    top: 228px; left: 0; right: 0;
    text-align: center;
    font-weight: 500;
    font-size: 30px;
    letter-spacing: 12px;
    color: var(--magenta);
    white-space: nowrap;
  }
  .benefit-line {
    position: absolute;
    top: 272px; left: 0; right: 0;
    text-align: center;
    font-weight: 700;
    font-size: 24px;
    letter-spacing: 0.5px;
    color: var(--ink);
    white-space: nowrap;
  }
  .variant-script {
    position: absolute;
    top: 330px; left: 0; right: 0;
    text-align: center;
    font-family: "Great Vibes", cursive;
    font-size: 96px;
    color: var(--mauve);
    line-height: 1;
  }
  .product-name {
    position: absolute;
    top: 375px; left: 0; right: 0;
    text-align: center;
    font-weight: 600;
    font-size: 112px;
    letter-spacing: 3px;
    color: var(--white);
    line-height: 1;
    white-space: nowrap;
  }
  .claim-band {
    position: absolute;
    top: 508px; left: 70px; right: 70px;
    height: 58px;
    border-radius: 29px;
    background: var(--magenta-dark);
    display: flex; align-items: center; justify-content: center; gap: 16px;
    font-weight: 700;
    font-size: 21px;
    letter-spacing: 1px;
    color: var(--white);
    white-space: nowrap;
  }
  .claim-divider {
    width: 2px; height: 30px;
    background: var(--white);
  }
  .mineral-note {
    position: absolute;
    top: 584px; left: 0; right: 0;
    text-align: center;
    font-weight: 600;
    font-size: 18px;
    letter-spacing: 4px;
    color: var(--white);
    white-space: nowrap;
  }
</style>
</head>
<body>

  <section class="lid-label" aria-label="Lid label">
    <svg viewBox="0 0 380 380" width="380" height="380">
      <defs>
        <mask id="pump-cutout">
          <rect width="380" height="380" fill="#fff"/>
          <circle cx="190" cy="40" r="125" fill="#000"/>
        </mask>
        <linearGradient id="lid-pink" x1="0" y1="0" x2="0" y2="1">
          <stop offset="0" stop-color="#fbe3ee"/>
          <stop offset="1" stop-color="#f5c6db"/>
        </linearGradient>
      </defs>
      <g mask="url(#pump-cutout)">
        <circle cx="190" cy="190" r="185" fill="url(#lid-pink)"/>
        <path d="M0 300 C110 270 260 310 380 278 L380 380 L0 380 Z" fill="#d6409a"/>
        <path d="M0 292 C110 262 260 302 380 270" fill="none" stroke="#fff" stroke-opacity="0.6" stroke-width="3"/>
      </g>
    </svg>
    <div class="lid-text">
      <div class="lid-script">Collagen</div>
      <div class="lid-title">BODY LOTION</div>
      <div class="lid-benefit">MOISTURIZING<br>FACE, NECK &amp; HANDS</div>
    </div>
  </section>

  <section class="front-label" aria-label="Front label">
    <svg class="label-bg" viewBox="0 0 1000 640" width="1000" height="640" preserveAspectRatio="none">
      <defs>
        <linearGradient id="blush-fill" x1="0" y1="0" x2="0" y2="1">
          <stop offset="0" stop-color="#fdf0f5"/>
          <stop offset="1" stop-color="#f5c6db"/>
        </linearGradient>
      </defs>
      <rect width="1000" height="640" fill="url(#blush-fill)"/>
      <path d="M0 120 C250 70 600 150 1000 60" fill="none" stroke="#fff" stroke-opacity="0.7" stroke-width="4"/>
      <path d="M0 355 C300 350 650 335 1000 305 L1000 640 L0 640 Z" fill="#d6409a"/>
      <path d="M0 340 C300 335 650 320 1000 290" fill="none" stroke="#fff" stroke-opacity="0.5" stroke-width="3"/>
    </svg>

    <div class="brand"><span>VELAINE</span><span class="brand-dot"></span></div>
    <div class="size-tag">PROFESSIONAL SIZE</div>
    <div class="benefit-line">MOISTURIZING FACE, NECK &amp; HANDS</div>
    <div class="variant-script">Collagen</div>
    <div class="product-name">BODY LOTION</div>
    <div class="claim-band">
      <span>VITAMIN C BRIGHTENING CREAM</span>
      <span class="claim-divider"></span>
      <span>16.9 FL OZ (500 ML)</span>
    </div>
    <div class="mineral-note">WITH DEAD SEA MINERALS</div>
  </section>

</body>
</html>
```